Stationary/business cards/letter head for IT Company
Vornel L.L.C.
Logo AI file uploaded.
Attention:
I've uploaded our current letter head with our old address. I would like to see stationary drafts with the top border (b/w picture) as seen in the PDF "letter head sample" uploaded. The picture taken is of the City of Phoenix Arizona at night.
Also, Please use black envelopes with a green flap.
Feel free to experiment.
RK/TPW/HN Team

```html
<!DOCTYPE html>
<html lang="en">
<head>
<meta charset="utf-8">
<title>Vornel L.L.C. Stationery</title>
<link rel="stylesheet" href="https://fonts.googleapis.com/css2?family=Open+Sans:wght@400;700;800&display=swap">
<style>
  :root {
    --bg: #3a3a3a;
    --ink: #141414;
    --ink-2: #1e1e1e;
    --green: #8cc63f;
    --green-dark: #6ea52a;
    --paper: #ffffff;
    --muted: #9a9a9a;
    --text-dark: #555555;
  }
  * { box-sizing: border-box; margin: 0; padding: 0; }
  html, body { width: 1200px; height: 686px; overflow: hidden; }
  body { background: var(--bg); font-family: "Open Sans", Arial, sans-serif; position: relative; }

  .piece { position: absolute; box-shadow: 0 3px 10px rgba(0,0,0,.45); overflow: hidden; }

  .brand { display: flex; align-items: center; gap: 7px; color: var(--green); font-weight: 800; letter-spacing: .04em; }
  .brand-dot { width: 14px; height: 14px; border-radius: 50%; background: var(--green); flex: none; }

  /* Envelope back */
  .envelope-back { left: 40px; top: 106px; width: 520px; height: 230px; background: var(--ink); }
  .envelope-flap { position: absolute; left: 0; top: 0; width: 100%; height: 46px; background: var(--green); }
  .envelope-flap .web { position: absolute; left: 0; right: 0; top: 16px; text-align: center; font-size: 9px; color: var(--ink); }
  .envelope-seam { position: absolute; left: 0; top: 46px; width: 100%; height: 2px; background: var(--green-dark); }

  /* Envelope front */
  .envelope-front { left: 40px; top: 375px; width: 520px; height: 228px; background: var(--ink); }
  .envelope-front .brand { position: absolute; left: 22px; top: 70px; font-size: 22px; }
  .envelope-front .brand-dot { width: 22px; height: 22px; }
  .stripe-band { position: absolute; top: 102px; height: 12px; background: var(--green); }
  .stripe-bars { position: absolute; display: flex; gap: 4px; }
  .stripe-bars span { display: block; height: 100%; background: var(--green); }
  .envelope-front .address { position: absolute; left: 22px; bottom: 26px; font-size: 7px; color: var(--muted); line-height: 1.5; }
  .label { color: var(--green); }
  .envelope-front .contacts { position: absolute; left: 318px; bottom: 22px; font-size: 7px; color: var(--muted); line-height: 1.5; }

  /* Business cards */
  .card { left: 588px; width: 144px; height: 162px; background: var(--ink-2); border-radius: 8px; }
  .card-front { top: 228px; }
  .card-back { top: 398px; }
  .card-front .brand-dot { position: absolute; left: 14px; top: 22px; width: 16px; height: 16px; }
  .card-front .band { position: absolute; left: 0; right: 0; top: 52px; height: 8px; background: var(--green); }
  .card-front .person { position: absolute; left: 14px; top: 72px; font-size: 6px; color: var(--muted); line-height: 1.5; }
  .card-front .person strong { color: #ddd; font-weight: 700; }
  .card-front .addr { position: absolute; left: 82px; top: 72px; font-size: 5.5px; color: var(--muted); line-height: 1.5; }
  .card-back .brand { position: absolute; right: 12px; top: 72px; font-size: 13px; }
  .card-back .brand-dot { width: 12px; height: 12px; }
  .card-back .tagline { position: absolute; left: 0; bottom: 26px; width: 96px; height: 10px; background: var(--green); color: var(--ink); font-size: 5px; font-weight: 700; line-height: 10px; padding-left: 8px; letter-spacing: .04em; }

  /* Letterhead */
  .letterhead { left: 749px; top: 41px; width: 404px; height: 595px; background: var(--paper); }
  .letterhead-header { position: absolute; left: 0; top: 0; width: 100%; height: 78px; background: #000; }
  .city-photo { position: absolute; right: 0; top: 0; width: 230px; height: 78px; background: linear-gradient(90deg, #000 0%, #2b2b2b 35%, #6d6d6d 70%, #8e8e8e 100%); }
  .letterhead-header .brand { position: absolute; left: 18px; top: 28px; font-size: 20px; }
  .letterhead-header .brand-dot { width: 20px; height: 20px; }
  .letterhead-header .band { position: absolute; left: 0; bottom: 0; width: 100%; height: 4px; background: var(--green); }
  .letterhead-footer { position: absolute; left: 0; right: 0; bottom: 0; height: 40px; }
  .letterhead-footer .contacts { position: absolute; left: 18px; top: 6px; font-size: 6px; color: var(--text-dark); line-height: 1.5; }
  .letterhead-footer .addr { position: absolute; left: 200px; top: 6px; font-size: 6px; color: var(--text-dark); line-height: 1.5; }
  .letterhead-footer .rule { position: absolute; left: 18px; right: 60px; bottom: 6px; height: 3px; background: var(--green); }
</style>
</head>
<body>

<section class="piece envelope-back">
  <div class="envelope-flap"><p class="web">web: www.vornelllc.com</p></div>
  <div class="envelope-seam"></div>
</section>

<section class="piece envelope-front">
  <div class="brand"><span class="brand-dot"></span>VORNEL</div>
  <div class="stripe-band" style="left:150px;width:250px;"></div>
  <div class="stripe-bars" style="left:408px;top:102px;height:12px;">
    <span style="width:6px"></span><span style="width:4px"></span><span style="width:3px"></span><span style="width:2px"></span><span style="width:2px"></span>
  </div>
  <div class="stripe-bars" style="left:460px;top:102px;height:12px;">
    <span style="width:4px"></span><span style="width:2px"></span><span style="width:6px"></span><span style="width:2px"></span>
  </div>
  <p class="address"><span class="label">Address</span><br>4410 W. Canyon Rd Suite 12 Mesa AZ 85201</p>
  <p class="contacts">
    <span class="label">Cell</span> 480-555-0142<br>
    <span class="label">Phone</span> 480-555-0187<br>
    <span class="label">Fax</span> 480-555-0163<br>
    <span class="label">Email</span> info@vornelllc.com
  </p>
</section>

<section class="piece card card-front">
  <span class="brand-dot"></span>
  <div class="band"></div>
  <p class="person"><strong>Dana L. Prior</strong><br>CEO<br><br>Cell 480-555-0142<br>Ph 480-555-0187<br>Fax 480-555-0163<br>info@vornelllc.com</p>
  <p class="addr"><span class="label">Address</span><br>4410 W. Canyon Rd<br>Mesa AZ 85201</p>
</section>

<section class="piece card card-back">
  <div class="brand"><span class="brand-dot"></span>VORNEL</div>
  <p class="tagline">BUILDING A BRIGHTER FUTURE</p>
</section>

<section class="piece letterhead">
  <header class="letterhead-header">
    <div class="city-photo" role="img" aria-label="Black and white photo of a city skyline at night"></div>
    <div class="brand"><span class="brand-dot"></span>VORNEL</div>
    <div class="band"></div>
  </header>
  <footer class="letterhead-footer">
    <p class="contacts"><span class="label">Cell</span> 480-555-0142 &nbsp; <span class="label">Phone</span> 480-555-0187<br><span class="label">Email</span> info@vornelllc.com</p>
    <p class="addr"><span class="label">Address</span><br>4410 W. Canyon Rd Suite 12 Mesa AZ 85201</p>
    <div class="rule"></div>
  </footer>
</section>

</body>
</html>
```